Support Welcome Packet Redesign

Looking to redesign our current "welcome packet" that we send to our new customers to help them understand our support service. It is currently in Microsoft Word and would like to remain in either word or publisher. Something that we can easily edit, as the content adjusts based on the customer needs. We want this document to be simple and understandable as it should be something our customers can reference at any time during our contract and easy to navigate.

Target Market(s)

Current Customers. Healthcare, Oil & Gas, Transportation, etc.

Industry/Entity Type

It Service

Font styles to use
Sans Serif

Requirements
Must have
• Table of Contents, bluQuay Logo and current content
Nice to have
• Easy navigation. Redone final page (contact info)

Files

```html
<!DOCTYPE html>
<html lang="en">
<head>
<meta charset="utf-8">
<title>Support Information</title>
<link href="https://fonts.googleapis.com/css2?family=Carlito:wght@400;700&display=swap" rel="stylesheet">
<style>
  :root{
    --orange:#f7761f;
    --ink:#1d1d1d;
    --row-alt:#f1f1f1;
    --rule:#e2e2e2;
    --bg:#ffffff;
    --blue:#2a8fd6;
    --green:#6cb33f;
    --yellow:#f5c400;
  }
  *{margin:0;padding:0;box-sizing:border-box}
  html,body{width:848px;height:1200px;overflow:hidden;background:var(--bg)}
  body{font-family:"Carlito",Calibri,Arial,sans-serif;color:var(--ink);position:relative}
  .page{position:relative;width:848px;height:1200px;overflow:hidden}
  .header-art{position:absolute;left:0;top:0}
  .page-title{position:absolute;left:80px;top:54px;color:#fff;font-weight:700;font-size:31px;text-shadow:1px 1px 2px rgba(0,0,0,.25);white-space:nowrap}
  .brand{position:absolute;left:696px;top:108px;display:flex;align-items:center;gap:6px;font-weight:700;font-size:24px;color:var(--orange);white-space:nowrap}
  .brand-square{width:14px;height:14px;background:var(--orange)}
  .guidelines{position:absolute;left:80px;top:304px;width:708px;font-size:18.6px;line-height:24px;text-align:justify}
  .guidelines h2{font-size:18.6px;font-weight:700;margin-bottom:10px}
  .guidelines ol{list-style:none}
  .guidelines li{margin-bottom:4.8px}
  .guidelines strong{font-weight:700}
  .priority-table{position:absolute;left:83px;top:793px;width:703px;border-collapse:collapse;font-size:15.5px;border:1px solid var(--rule)}
  .priority-table th{background:var(--orange);color:#fff;font-weight:700;height:41px;border-right:1px solid #fa9a55;white-space:nowrap}
  .priority-table td{height:29.5px;text-align:center;color:#333;border-bottom:1px solid var(--rule);white-space:nowrap}
  .priority-table td.level{text-align:left;padding-left:19px;font-weight:700}
  .priority-table tr:nth-child(even) td{background:var(--row-alt)}
  .footer{position:absolute;left:0;top:1064px;width:848px;height:24px;font-size:13.5px;color:#333}
  .footer > div{position:absolute;top:0;height:24px;display:flex;align-items:center;gap:5px;white-space:nowrap}
  .footer-brand{left:53px;font-weight:700;font-size:17px;color:var(--orange)}
  .footer-brand .sq{width:11px;height:11px;background:var(--orange)}
  .contact-address{left:246px}
  .contact-phone{left:490px}
  .contact-web{left:612px}
  .contact svg{flex:none}
  .color-bar{position:absolute;left:8px;top:1099px;width:840px;height:6px;background:linear-gradient(90deg,var(--blue) 0%,#9fd0ef 20%,var(--green) 32%,var(--yellow) 45%,var(--orange) 58%,var(--yellow) 72%,var(--green) 100%)}
  .page-number{position:absolute;left:774px;top:1115px;font-size:19px}
</style>
</head>
<body>
<main class="page">
  <svg class="header-art" width="848" height="290" viewBox="0 0 848 290">
    <defs>
      <linearGradient id="haze" x1="0" y1="0" x2="0" y2="1">
        <stop offset="0" stop-color="#e6e6e6"/>
        <stop offset="1" stop-color="#ffffff"/>
      </linearGradient>
    </defs>
    <rect width="848" height="290" fill="url(#haze)"/>
    <circle cx="300" cy="160" r="92" fill="var(--orange)" role="img" aria-label="Decorative orange gear"/>
    <circle cx="260" cy="90" r="40" fill="var(--orange)" opacity=".85" role="img" aria-label="Decorative small gear"/>
    <polygon points="0,0 500,0 590,110 0,110" fill="var(--orange)"/>
    <polyline points="498,0 732,254 848,156" fill="none" stroke="var(--orange)" stroke-width="4"/>
  </svg>
  <h1 class="page-title">Support Information</h1>
  <div class="brand"><span class="brand-square"></span>bluQuay</div>

  <section class="guidelines">
    <h2>Escalation Guidelines</h2>
    <ol>
      <li>1.&nbsp;&nbsp;&nbsp; When an incident is reported, a ticket is generated and you, the customer are provided with the ticket number or other reference for the ticket.</li>
      <li>2.&nbsp;&nbsp;&nbsp; <strong>bluQuay</strong> will assign a priority to each incident based on customer input and the priority matrix below.</li>
      <li>3.&nbsp;&nbsp;&nbsp; We will provide the first response to the ticket in accordance with the priority matrix below.</li>
      <li>4.&nbsp;&nbsp; Every incident is first addressed by the Technical Support Team.</li>
      <li>5.&nbsp;&nbsp; If the Technical Support Team is not able to resolve the incident, it is escalated to the Network Engineering Team.&nbsp; If the incident is Priority 2 or higher, it is directly escalated to the Network Engineering Team.</li>
      <li>6.&nbsp;&nbsp; If Network Engineering Team is not able to resolve the incident in two (2) business days, the incident is escalated to the Architecture/Development Team.</li>
      <li>7.&nbsp;&nbsp; The Architecture/Development Team will provide a solution or workaround inside the timeframe of the solution objective.</li>
      <li>8.&nbsp;&nbsp; Every incident is updated on a daily basis.</li>
    </ol>
  </section>

  <table class="priority-table">
    <colgroup><col style="width:89px"><col style="width:182px"><col style="width:192px"><col></colgroup>
    <thead><tr><th>Priority</th><th>Solution Objective</th><th>Response Objective</th><th>Assigned Team</th></tr></thead>
    <tbody>
      <tr><td class="level">Level 1</td><td>24 Hours</td><td>1 Hour</td><td>Architect/Development</td></tr>
      <tr><td class="level">Level 2</td><td>2 Days</td><td>4 Hours</td><td>Network Engineers</td></tr>
      <tr><td class="level">Level 3</td><td>5 Days</td><td>4 Hours</td><td>Support Team</td></tr>
      <tr><td class="level">Level 4</td><td>14 Days</td><td>1 Day</td><td>Support Team</td></tr>
    </tbody>
  </table>

  <footer class="footer">
    <div class="footer-brand"><span class="sq"></span>bluQuay Technology</div>
    <div class="contact contact-address">
      <svg width="13" height="18" viewBox="0 0 14 20"><path d="M7 0a7 7 0 0 0-7 7c0 5 7 13 7 13s7-8 7-13a7 7 0 0 0-7-7zm0 10a3 3 0 1 1 0-6 3 3 0 0 1 0 6z" fill="var(--blue)"/></svg>
      420 W Linden Ave&nbsp; Tempe, AZ 85281
    </div>
    <div class="contact contact-phone">
      <svg width="15" height="17" viewBox="0 0 16 18"><path d="M3 1l3 0 1 4-2 1.5c1 2.5 2.5 4.5 5 6L11.5 10.5l4 1v3.5c0 1-1 2-2 2C6 16.5 1 10 1 3c0-1 1-2 2-2z" fill="var(--blue)"/></svg>
      480-555-0192
    </div>
    <div class="contact contact-web">
      <svg width="17" height="17" viewBox="0 0 18 18"><circle cx="9" cy="9" r="8" fill="var(--blue)"/><path d="M5 5c2 0 3 2 2 3s-2 2 0 4M12 3c-1 2 1 3 2 4M11 11c1 1 2 2 1 4" stroke="#fff" stroke-width="1.5" fill="none"/></svg>
      www.BLUQUAYCORP.com
    </div>
  </footer>
  <div class="color-bar"></div>
  <div class="page-number">7</div>
</main>
</body>
</html>
```